FULL Stationary & Business Cards for Innovative Software Company
Stationary/Business Card/Email Signatures
FULL Stationary & Business Cards for Innovative Software Company - Software
Creative Brief
Professional
Miles Tenvard
Managing Partner
412 Harrow Bend Road Suite 309, North Annex Mississauga, ON L4T 2K8
milest@quelvoworks.example
www.quelvoworks.example
restwzeasy restwzeasy
Please submit all of your final stationary designs. We are making a decision soon.
sevensky sevensky
Please tell which design no we use to make stationary package??
Can you please submit full stationary for the designs that were evaluated with stars?
Watermark logo on back of the card is very interesting.
The cards must show all of the provided contact information. Some of the designs only show the telephone without the address.
The front of the card should be easy to read, but also be interesting. All white on the front is little boring.
We like the designs with the back of the card in red instead of blue.
We are not very interested in a border on the front of the card.
Check #140, also its a veiled contest, no one can see other designs, so kindly send a comment/feedback through private messeging service of panelhive, thanks! regards
design #132, looks better, but little plain on the front page.
We like the designs with some creative content on the front, but not too intrusive. We are not very interested in all white front of the card - we feel that is too plan. At the same time, the design should complement the information, not distract from it. Please continue to submit your designs. Innovative, fresh, professional are some of the characteristics we are trying to communicate.
On the folder designs, please be little more creative. A lot of them look plain. We are trying to communicate that we are an interesting, innovative, leading edge software company.
#81, the content is all in the centre of the card. Please try to spread the content around the card.
We like the back designs with only the logo instead of having the contact information.
We like the designs that make use of the space instead of all of the text being grouped in one specific area of the card leaving 1/2 of the business card space obviously empty. It should be easy for someone to quickly scan the card and see the name, address, and contact information instead of having to search for it.
We like the red back of the card better than the blue.
Please use the Quelvo logo without the "TM" (trademark).
Xpert Xpert
Sir, can you give some star rating first then we move towards stationery to the rated designs. Thanks
Thank you for the designs, but please keep in mind that the request is for all stationary including 2 sided business cards, letterhead, envelopes, email signature, and portfolio.

```html
<!DOCTYPE html>
<html lang="en">
<head>
<meta charset="utf-8">
<title>Quelvo Stationery Set</title>
<link href="https://fonts.googleapis.com/css2?family=Open+Sans:wght@400;700&display=swap" rel="stylesheet">
<style>
  :root {
    --bg: #5c5c5e;
    --red: #9c1c22;
    --red-dark: #861519;
    --red-faint: #a9262c;
    --paper: #ffffff;
    --ink: #6d6e71;
    --ink-light: #d9d9db;
    --accent-blue: #3f63a8;
  }
  * { box-sizing: border-box; margin: 0; padding: 0; }
  html, body { width: 1200px; height: 365px; overflow: hidden; background: var(--bg); }
  body { position: relative; font-family: "Open Sans", Arial, sans-serif; color: var(--ink); }
  .piece { position: absolute; background: var(--paper); overflow: hidden; }
  .piece.red { background: var(--red); }
  .brand { font-family: "Open Sans", Arial, sans-serif; font-weight: 700; color: var(--red); line-height: 1; white-space: nowrap; }
  .brand.light { color: var(--paper); }
  .tagline { font-size: 7px; color: var(--ink); line-height: 1.3; }
  .tagline.light { color: var(--paper); }
  .small { font-size: 3px; line-height: 1.35; color: var(--ink); }
  .watermark { position: absolute; font-family: "Open Sans", Arial, sans-serif; font-weight: 700; line-height: 1; white-space: nowrap; }
  .stripe { position: absolute; left: 0; right: 0; height: 3px; background: var(--red); }
  .stripe::after { content: ""; position: absolute; left: 0; right: 0; top: 3px; height: 1px; background: var(--accent-blue); }

  .card-front { left: 29px; top: 115px; width: 67px; height: 38px; }
  .card-front .brand { position: absolute; left: 4px; top: 5px; font-size: 6px; }
  .card-front .contact { position: absolute; right: 4px; top: 15px; text-align: right; font-size: 2.4px; }
  .card-front .stripe { bottom: 3px; height: 2px; }
  .card-back { left: 29px; top: 180px; width: 67px; height: 40px; display: flex; align-items: center; justify-content: center; }
  .card-back .brand { font-size: 9px; }

  .letterhead { left: 108px; top: 53px; width: 188px; height: 240px; }
  .letterhead .brand { position: absolute; right: 12px; top: 14px; font-size: 8px; }
  .letterhead .address { position: absolute; right: 12px; top: 25px; text-align: right; width: 80px; }
  .letterhead .watermark { left: 0; right: 0; top: 102px; text-align: center; font-size: 26px; color: var(--ink-light); }
  .letterhead .stripe { bottom: 6px; }

  .slip { left: 307px; top: 53px; width: 173px; height: 43px; }
  .slip .brand { position: absolute; left: 8px; top: 8px; font-size: 7px; }
  .slip .note { position: absolute; left: 8px; top: 22px; font-size: 4px; }
  .slip .address { position: absolute; right: 8px; top: 8px; text-align: right; width: 64px; }
  .slip .stripe { bottom: 2px; height: 2px; }

  .envelope-front { left: 307px; top: 120px; width: 173px; height: 77px; }
  .envelope-front .brand { position: absolute; left: 8px; top: 8px; font-size: 8px; }
  .envelope-front .address { position: absolute; left: 8px; top: 20px; width: 60px; }
  .envelope-front .stripe { bottom: 3px; }
  .envelope-back { left: 307px; top: 210px; width: 173px; height: 82px; }
  .envelope-back svg { position: absolute; inset: 0; }

  .folder-outer { left: 500px; top: 46px; width: 197px; height: 272px; }
  .folder-outer svg { position: absolute; inset: 0; }
  .folder-outer .logo { position: absolute; left: 0; right: 0; top: 140px; text-align: center; }
  .folder-outer .brand { font-size: 14px; }
  .folder-outer .watermark { left: 8px; top: 205px; font-size: 34px; color: var(--red-faint); }
  .folder-inner { left: 697px; top: 46px; width: 197px; height: 272px; }
  .folder-inner .logo { position: absolute; left: 0; right: 0; top: 140px; text-align: center; }
  .folder-inner .brand { font-size: 19px; }

  .disc { position: absolute; left: 955px; top: 45px; width: 134px; height: 134px; border-radius: 50%; background: var(--paper); }
  .disc .hole { position: absolute; left: 55px; top: 55px; width: 24px; height: 24px; border-radius: 50%; background: var(--bg); border: 4px solid #e6e6e8; }
  .disc .logo { position: absolute; left: 0; right: 0; top: 86px; text-align: center; }
  .disc .brand { font-size: 15px; }
  .disc .tagline { font-size: 6px; }

  .sleeve { left: 893px; top: 204px; width: 283px; height: 108px; }
  .sleeve .watermark { left: 6px; top: 62px; font-size: 32px; color: var(--red-faint); }
  .sleeve .panel { position: absolute; left: 118px; top: 16px; width: 157px; height: 80px; background: var(--paper); display: flex; flex-direction: column; align-items: center; justify-content: center; }
  .sleeve .brand { font-size: 17px; }
</style>
</head>
<body>
  <section class="piece card-front">
    <div class="brand">QUELVO</div>
    <div class="small contact">Miles Tenvard<br>Managing Partner<br>412 Harrow Bend Road Suite 309<br>milest@quelvoworks.example<br>www.quelvoworks.example</div>
    <div class="stripe"></div>
  </section>
  <section class="piece red card-back">
    <div class="brand light">QUELVO</div>
  </section>

  <section class="piece letterhead">
    <div class="brand">QUELVO</div>
    <div class="small address">412 Harrow Bend Road Suite 309, North Annex Mississauga, ON L4T 2K8<br>www.quelvoworks.example</div>
    <div class="watermark">QUELVO</div>
    <div class="stripe"></div>
  </section>

  <section class="piece slip">
    <div class="brand">QUELVO</div>
    <div class="note">With Compliments</div>
    <div class="small address">412 Harrow Bend Road Suite 309<br>North Annex Mississauga, ON L4T 2K8<br>www.quelvoworks.example</div>
    <div class="stripe"></div>
  </section>

  <section class="piece envelope-front">
    <div class="brand">QUELVO</div>
    <div class="small address">412 Harrow Bend Road Suite 309, North Annex Mississauga, ON L4T 2K8</div>
    <div class="stripe"></div>
  </section>
  <section class="piece envelope-back">
    <svg width="173" height="82" viewBox="0 0 173 82">
      <polygon points="0,0 173,0 173,6 96,48 77,48 0,6" fill="var(--red)"/>
      <line x1="0" y1="82" x2="70" y2="38" stroke="#e4e4e6" stroke-width="0.8"/>
      <line x1="173" y1="82" x2="103" y2="38" stroke="#e4e4e6" stroke-width="0.8"/>
    </svg>
  </section>

  <section class="piece red folder-outer">
    <svg width="197" height="272" viewBox="0 0 197 272">
      <path d="M0 215 L70 215 L84 232 L197 232 L197 272 L0 272 Z" fill="var(--red-dark)"/>
      <path d="M60 248 L98 248 L98 258 L60 258 Z" fill="none" stroke="var(--red-faint)" stroke-width="1"/>
    </svg>
    <div class="watermark">QUELVO</div>
    <div class="logo"><div class="brand light">QUELVO</div><div class="tagline light">Software Labs</div></div>
  </section>
  <section class="piece folder-inner">
    <div class="logo"><div class="brand">QUELVO</div><div class="tagline">Software Labs</div></div>
  </section>

  <section class="disc">
    <div class="hole"></div>
    <div class="logo"><div class="brand">QUELVO</div><div class="tagline">Software Labs</div></div>
  </section>

  <section class="piece red sleeve">
    <div class="watermark">QUELVO</div>
    <div class="panel"><div class="brand">QUELVO</div><div class="tagline">Software Labs</div></div>
  </section>
</body>
</html>
```